Catalogue Design Project

Hi all,

I would like to design Catalogue for our Range Hood products. I am looking for help to design a elegant catalogue impress our potential customer.

Thanks,

Marek

Target Market(s)

Our customers are in US, Canada as well as Australia.

Requirements
Must have
• Please used the pictures of range hood models from the attached file (6 models.rar). Our company information.

Nice to have
• It is nice if the cataloge design as a book style.

```html
<!DOCTYPE html>
<html lang="en">
<head>
<meta charset="utf-8">
<title>RangeHood 04 – Catalogue Page</title>
<link href="https://fonts.googleapis.com/css2?family=Exo+2:wght@300;400;600&display=swap" rel="stylesheet">
<style>
  :root {
    --ink: #111111;
    --accent-red: #d0161b;
    --muted-grey: #a3a3a3;
    --body-text: #2a2a2a;
    --page: #fdfdfd;
    --mint-top: #fbfdfb;
    --mint-bottom: #e2f5e6;
    --teal-rule: #7fe3c9;
  }
  * { margin: 0; padding: 0; box-sizing: border-box; }
  html, body { width: 1200px; height: 846px; overflow: hidden; }
  body {
    background: var(--page);
    font-family: "Exo 2", sans-serif;
    color: var(--body-text);
    position: relative;
  }
  .page-header {
    position: absolute;
    left: 55px;
    top: 34px;
    font-size: 24px;
    font-weight: 400;
    color: var(--ink);
    letter-spacing: 0.2px;
  }
  .page-header .accent { color: var(--accent-red); font-weight: 600; }
  .header-rule {
    position: absolute;
    left: 243px;
    top: 45px;
    width: 957px;
    height: 14px;
  }
  .product-visual {
    position: absolute;
    left: 368px;
    top: 318px;
    right: 0;
    height: 460px;
    background: linear-gradient(160deg, var(--mint-top) 0%, #f1faf2 45%, var(--mint-bottom) 100%);
    border-bottom: 1px solid var(--teal-rule);
  }
  .product-visual .hood-shape {
    position: absolute;
    left: 52px;
    top: 122px;
    width: 642px;
    height: 204px;
    background: linear-gradient(180deg, #d9dcdc 0%, #bfc3c4 55%, #9ea3a5 100%);
    border-radius: 4px;
    opacity: 0.55;
  }
  .spec-sheet {
    position: absolute;
    left: 56px;
    top: 379px;
    width: 300px;
  }
  .spec-sheet .model-name {
    font-size: 30px;
    font-weight: 600;
    color: var(--muted-grey);
    margin-bottom: 12px;
  }
  .spec-group { list-style: none; font-size: 15px; line-height: 22px; font-weight: 300; }
  .spec-group + .spec-group, .spec-group + .options-title { margin-top: 22px; }
  .spec-group .label { font-weight: 600; color: var(--ink); }
  .options-title {
    font-size: 15px;
    line-height: 22px;
    font-weight: 600;
    color: var(--accent-red);
  }
</style>
</head>
<body>
  <header class="page-header">Range <span class="accent">Hood 04</span></header>
  <svg class="header-rule" viewBox="0 0 957 14" preserveAspectRatio="none" aria-hidden="true">
    <rect x="1" y="2.5" width="8" height="8" fill="none" stroke="#111" stroke-width="1.6"/>
    <line x1="10" y1="5" x2="957" y2="5" stroke="#111" stroke-width="1.8"/>
    <line x1="10" y1="9" x2="957" y2="9" stroke="#d0161b" stroke-width="0.8"/>
  </svg>

  <div class="product-visual" role="img" aria-label="Product photo: stainless steel under-cabinet range hood with black touch control panel and aluminium baffle filters">
    <div class="hood-shape"></div>
  </div>

  <section class="spec-sheet">
    <h2 class="model-name">RangeHood 04</h2>
    <ul class="spec-group">
      <li><span class="label">Control</span> Cap. Touch 3 Speed</li>
      <li><span class="label">Display</span> LCD Indicates</li>
      <li><span class="label">Gross Weight</span> 11kg</li>
      <li><span class="label">Dimension</span> 755x255x250mm</li>
    </ul>
    <ul class="spec-group">
      <li><span class="label">Body</span> Non-magnetic</li>
      <li>High Quality Stainless Steel</li>
      <li><span class="label">Lighting</span> 2 x LED Lights - 120lm</li>
      <li><span class="label">Motor</span> 2 x 120W - 443m 3/h</li>
      <li><span class="label">Filter</span> 2 x Aluminium Filters</li>
    </ul>
    <h3 class="options-title">Optional Features</h3>
    <ul class="spec-group options-list">
      <li>IR Remote Control</li>
      <li>Gas Sensor</li>
      <li>Autoclean Function</li>
      <li>Charcoal Feature</li>
    </ul>
  </section>
</body>
</html>
```